Olive oil bottle labels, front and back.

Sophisticated uncluttered distinctive eye catching label
Front label:
Label on front like the uploaded file in design but called “Corrowick Hollow”, (not Marrabel Reach.)
Need to state that it’s extra virgin, cold pressed olive oil, 100% organic, grown and pressed on the Kesterly Peninsula.
500 ml
Back label:
Nutritional information table (see label example in uploaded files) including FFA 0.1% Oleic Acid
Storage: airtight in cool dark place
Made and produced in Australia from 100% Australian ingredients,
Harvest date:
Best by:
Batch:
Grown, harvested and bottled at The Hollow, Pellandry Rd. Varrendale. 3847
The back label on uploaded files has the info requited except they should have address and don't include those industry and Australian made logos.
The front label is what we want, first to plagiarise without copyright infringement gets the gig, thanks.
Labels front and back need be 5 x 13 cm
Gourmet, up-market
- Love "Adorn Regular Garland"

```html
<!DOCTYPE html>
<html lang="en">
<head>
<meta charset="utf-8">
<title>Corrowick Hollow Olive Oil Labels</title>
<link rel="stylesheet" href="https://fonts.googleapis.com/css2?family=Fira+Sans:wght@300;400;500;600&family=Source+Serif+4:wght@600&display=swap">
<style>
  :root {
    --backdrop: #7d7672;
    --label-gold: #9c8434;
    --band-black: #151412;
    --ink: #1d1a12;
    --white: #ffffff;
    --sans: "Fira Sans", Arial, sans-serif;
    --serif: "Source Serif 4", Georgia, serif;
  }
  * { margin: 0; padding: 0; box-sizing: border-box; }
  html, body { width: 1197px; height: 1200px; overflow: hidden; }
  body { background: var(--backdrop); position: relative; font-family: var(--sans); color: var(--ink); }

  .label {
    position: absolute; top: 157px; width: 355px; height: 924px;
    background: var(--label-gold); overflow: hidden;
  }
  .label--front { left: 140px; }
  .label--back { left: 702px; }

  /* Front label */
  .brand-band {
    position: absolute; left: 0; top: 0; width: 96px; height: 100%;
    background: var(--band-black);
  }
  .brand-vertical {
    position: absolute; left: 44px; top: 912px;
    transform: rotate(-90deg); transform-origin: 0 0;
    white-space: nowrap; color: var(--white);
    font-family: var(--sans); font-weight: 300; font-size: 92px;
    letter-spacing: 4px; line-height: 1;
  }
  .front-copy { position: absolute; right: 40px; text-align: right; }
  .descriptor {
    top: 379px; color: var(--white); font-weight: 600; font-size: 14px;
    letter-spacing: 1.6px; line-height: 20px;
  }
  .product-name {
    top: 424px; font-family: var(--serif); font-weight: 600; font-size: 44px;
    line-height: 44px; color: var(--ink);
  }
  .organic-mark {
    position: absolute; left: 260px; top: 656px; width: 56px; height: 56px;
    border: 1.5px solid var(--white); border-radius: 50%;
  }
  .origin {
    top: 721px; color: var(--white); font-size: 16px; line-height: 21px;
  }
  .volume { top: 806px; font-size: 25px; font-weight: 300; color: var(--ink); }

  /* Back label */
  .back-content { position: absolute; left: 41px; width: 269px; top: 0; text-align: center; }
  .brand-small {
    margin-top: 70px; color: var(--white); font-size: 19px; font-weight: 300; letter-spacing: 2px;
  }
  .section-title { font-size: 18.5px; font-weight: 500; letter-spacing: 0.3px; }
  .nutrition-title { margin-top: 20px; }
  .nutrition-table {
    margin-top: 12px; width: 100%; border-collapse: collapse; font-size: 14.5px; font-weight: 300;
    border-top: 1.5px solid var(--ink); border-bottom: 1.5px solid var(--ink);
  }
  .nutrition-table td, .nutrition-table th { text-align: right; font-weight: 300; padding: 0 4px; line-height: 19.9px; }
  .nutrition-table .nutrient { text-align: left; }
  .nutrition-table .sub { padding-left: 12px; }
  .nutrition-table thead th { padding-top: 7px; padding-bottom: 2px; border-bottom: 1.5px solid var(--ink); vertical-align: top; }
  .nutrition-table tbody tr:first-child td { padding-top: 5px; }
  .nutrition-table tbody tr:last-child td { padding-bottom: 4px; }
  .ingredients-title { margin-top: 8px; }
  .back-text { font-size: 15px; font-weight: 300; line-height: 20px; }
  .storage { margin-top: 7px; color: var(--white); font-size: 14.5px; font-weight: 400; padding-bottom: 5px; border-bottom: 1.5px solid var(--ink); margin-left: -3px; margin-right: -3px; }
  .made-in { padding: 9px 0 6px; border-bottom: 1.5px solid var(--ink); }
  .grown-at { padding-top: 8px; }
  .batch-box {
    position: absolute; left: 63px; top: 812px; width: 229px; height: 66px;
    background: var(--white); padding: 4px 10px; font-size: 15px; line-height: 20px; color: var(--ink);
  }
</style>
</head>
<body>

<section class="label label--front" aria-label="Front label">
  <div class="brand-band"></div>
  <div class="brand-vertical">Corrowick Hollow</div>
  <p class="front-copy descriptor">EXTRA VIRGIN<br>COLD PRESSED</p>
  <h1 class="front-copy product-name">OLIVE<br>OIL</h1>
  <div class="organic-mark" role="img" aria-label="Organic certification badge"></div>
  <p class="front-copy origin">Grown and pressed<br>on the Kesterly<br>Peninsula</p>
  <p class="front-copy volume">500ml</p>
</section>

<section class="label label--back" aria-label="Back label">
  <div class="back-content">
    <p class="brand-small">Corrowick Hollow</p>
    <h2 class="section-title nutrition-title">NUTRITION INFORMATION</h2>
    <table class="nutrition-table">
      <thead>
        <tr><th class="nutrient">AVG QTY</th><th>PER<br>15ml</th><th>PER<br>100ml</th></tr>
      </thead>
      <tbody>
        <tr><td class="nutrient">ENERGY (KJ)</td><td>517</td><td>3446</td></tr>
        <tr><td class="nutrient">PROTEIN (G)</td><td>0</td><td>0</td></tr>
        <tr><td class="nutrient">FAT</td><td></td><td></td></tr>
        <tr><td class="nutrient sub">- Total</td><td>13.7</td><td>91.5</td></tr>
        <tr><td class="nutrient sub">- Saturated</td><td>2.1</td><td>14.1</td></tr>
        <tr><td class="nutrient sub">- Monounsaturated</td><td>10.7</td><td>71.5</td></tr>
        <tr><td class="nutrient sub">- Polyunsaturated</td><td>0.9</td><td>5.9</td></tr>
        <tr><td class="nutrient sub">- Trans Fatty Acid</td><td>&lt;0.01</td><td>&lt;0.05</td></tr>
        <tr><td class="nutrient sub">- FFA (Oleic Acid)</td><td>0.1</td><td>0.5</td></tr>
        <tr><td class="nutrient">CHOLESTEROL (MG)</td><td>0</td><td>0</td></tr>
        <tr><td class="nutrient">CARBONHYDRATE (G)</td><td>0</td><td>0</td></tr>
        <tr><td class="nutrient sub">- Sugar (G)</td><td>0</td><td>0</td></tr>
      </tbody>
    </table>
    <h2 class="section-title ingredients-title">INGREDIENTS</h2>
    <p class="back-text">100% Australian Extra virgin olive oil<br>(Cold pressed fresh)</p>
    <p class="storage">STORE AIRTIGHT IN A COOL DARK PLACE</p>
    <p class="back-text made-in">Made in Australia from 100%<br>Australian ingredients</p>
    <p class="back-text grown-at">Grown, harvest and bottled at the<br>Hollow, Pellandry Rd. Varrendale. 3847</p>
  </div>
  <div class="batch-box">Harvest date:<br>Best by:<br>Batch:</div>
</section>

</body>
</html>
```